Help us Create Excitement with a Food To Go Web Site Menu

We are seeking a design that can serve as a template for a Wordpress based website. The template will present the name (BrimBowl), present the menu items with price details, and contact details. The final design should NOT have the Market Lane Eats subtitle anywhere in the site.
Our plan is to have the menu with basic graphic elements with the options to link to images/pictures of the menu item (perhaps linked via Snapgrid or something like that if possible).
Updates

Target Market(s)

Home dining menu intended to offer perspective customers an understanding of what they will be enjoying.

Contact Information for Business Card

BrimBowl logo (without the Market Lane Eats tag line included)
hi@brimbowl.com.au
Phone: XXXX XXX XXX (to be provided)

Coding

Coded - Design and coding required

Number of Pages Required

2 page

Requirements
Must have
• A bold and colourful presence that is also on the playful side.

A clearly readable menu layout that doesn't feel small based on the limited number of items that we offer at this time.
Nice to have
• A playful semi-graffiti based feel would be nice to convey a sense of playfulness.
Should not have
• The design should not have an overly Asian feel to it.

It appears many people are misreading the brief so I am adding this point to clarify one of the design requirements.
-- The final design should NOT have the Market Lane Eats subtitle anywhere in the site, including the logo.

```html
<!DOCTYPE html>
<html lang="en">
<head>
<meta charset="utf-8">
<title>BrimBowl — Home Dining Delivery</title>
<link rel="stylesheet" href="https://fonts.googleapis.com/css2?family=Montserrat:wght@500;600;700;800;900&family=Open+Sans:wght@400;600&display=swap">
<style>
:root{
  --red:#d90000;
  --red-deep:#c40000;
  --black:#000;
  --ink:#111;
  --white:#fff;
  --grey-text:#6a6a6a;
  --band:#dcdcdc;
  --band-light:#efefef;
  --line:#bdbdbd;
}
*{box-sizing:border-box;margin:0;padding:0}
html,body{width:1200px;height:3417px;overflow:hidden;background:var(--white)}
body{position:relative;font-family:'Open Sans',sans-serif;color:var(--ink)}
.abs{position:absolute}
.heading{font-family:'Montserrat',sans-serif;font-weight:800;text-transform:uppercase;letter-spacing:.5px}
.btn{position:absolute;display:flex;align-items:center;justify-content:center;border-radius:40px;font-family:'Montserrat',sans-serif;font-weight:700;text-transform:uppercase;text-decoration:none}
.btn--red{background:var(--red);color:var(--white)}
.btn--white{background:var(--white);color:var(--ink)}
.placeholder{position:absolute}
svg.icon{width:18px;height:18px;vertical-align:-2px;fill:currentColor}

/* hero */
.hero-bg{position:absolute;left:0;top:0;width:1200px;height:780px}
.brand{left:108px;top:50px;font-family:'Montserrat',sans-serif;font-weight:900;font-size:56px;color:var(--white);display:flex;align-items:center;gap:14px}
.brand-dot{width:22px;height:22px;border-radius:50%;background:var(--white)}
.topbar{right:112px;top:18px;color:var(--white);font-family:'Montserrat',sans-serif;font-weight:600;font-size:18px;display:flex;gap:16px;align-items:center}
.nav{right:108px;top:66px;display:flex;gap:26px;font-family:'Montserrat',sans-serif;font-weight:700;font-size:18px}
.nav a{color:var(--white);text-decoration:none}
.nav a.active{color:#ff2a2a}
.hero-title{left:104px;top:192px;color:var(--white);font-size:80px;line-height:86px}
.hero-bowl{left:527px;top:100px;width:530px;height:530px;border-radius:50%;background:radial-gradient(circle at 50% 50%,#4a9c3a 0%,#6fa050 40%,#b8a98a 60%,#f4f4f4 64%,#e6e6e6 100%)}

/* welcome */
.veg{left:0;top:736px;width:597px;height:630px;background:radial-gradient(ellipse at 50% 50%,#7b3b6a 0%,#5f8a3a 45%,rgba(255,255,255,0) 75%)}
.welcome-title{left:634px;top:798px;font-size:48px;line-height:60px;color:var(--ink);font-weight:900}
.welcome-text{left:634px;top:936px;width:470px;font-size:15.5px;line-height:30px;color:var(--grey-text)}
.avatar{left:629px;top:1292px;width:126px;height:126px;border-radius:50%;background:linear-gradient(135deg,#3b2a22,#8a6b57);border:4px solid #222}
.signature{left:778px;top:1330px;width:150px;height:46px;background:linear-gradient(90deg,#444,#777);opacity:.35;border-radius:6px}

/* menu */
.menu-band{position:absolute;left:0;top:1400px;width:1200px;height:830px}
.menu-title{left:109px;top:1522px;font-size:46px;font-weight:900}
.dish-name{left:109px;top:1600px;font-family:'Montserrat',sans-serif;font-weight:500;font-size:33px;color:#333}
.dish-price{left:110px;top:1655px;font-family:'Montserrat',sans-serif;font-weight:700;font-size:24px;color:var(--red)}
.dish-text{left:107px;top:1698px;width:460px;font-size:14.5px;line-height:27.5px;color:#555}
.menu-contact{left:110px;top:2058px;font-family:'Montserrat',sans-serif;font-weight:500;font-size:21px;display:flex;gap:12px;align-items:center}
.menu-contact svg{fill:var(--red);width:20px;height:20px}
.browse{left:111px;top:2108px;font-family:'Montserrat',sans-serif;font-weight:700;font-size:17px;color:var(--red);text-decoration:underline}
.arrow{position:absolute;top:2104px;width:32px;height:32px;border-radius:50%;background:#555;display:flex;align-items:center;justify-content:center}
.arrow svg{width:16px;height:16px;fill:none;stroke:#fff;stroke-width:3}
.rolls{left:623px;top:1440px;width:600px;height:715px;border-radius:50% 0 0 50%;background:radial-gradient(ellipse at 45% 55%,#e8d8dc 0%,#b98a76 35%,#2f6f2a 62%,#9a9a9a 78%,rgba(220,220,220,0) 100%)}

/* contact form */
.touch-title{left:0;width:1200px;top:2242px;text-align:center;font-size:48px;font-weight:900}
.leaf{left:880px;top:2236px;width:320px;height:290px;border-radius:60% 10% 60% 20%;background:linear-gradient(135deg,#3f8a2c,#1f5a1a)}
.form-card{left:111px;top:2350px;width:978px;height:498px;background:var(--white);box-shadow:0 2px 10px rgba(0,0,0,.15)}
.form-photo{left:111px;top:2350px;width:373px;height:498px;background:radial-gradient(ellipse at 55% 45%,#f3ead6 0%,#e4c69a 40%,#8a5a2e 85%)}
.label{position:absolute;font-size:15px;color:#555}
.field{position:absolute;border:1px solid #aaa;background:#fff}
.agree{left:513px;top:2744px;font-size:15px;color:#555;display:flex;align-items:center;gap:10px}
.agree span.box{width:14px;height:14px;border:1px solid #555;border-radius:2px}

/* footer */
.footer-bg{position:absolute;left:0;top:2860px;width:1200px;height:557px}
.foot-heading{font-family:'Montserrat',sans-serif;font-weight:700;font-size:20px;color:var(--white);text-transform:uppercase}
.map{left:111px;top:3104px;width:321px;height:194px;background:linear-gradient(135deg,#eef1ea,#dfe6d6)}
.foot-line{color:var(--white);font-size:16px;display:flex;gap:10px;align-items:center}
.social{position:absolute;top:3221px;width:42px;height:42px;border-radius:50%;border:1px solid #777}
.noodles{left:769px;top:2904px;width:460px;height:404px;border-radius:50%;background:radial-gradient(circle at 50% 50%,#f4ead0 0%,#d9c49a 40%,#5f8f3a 65%,rgba(30,30,30,0) 75%)}
.divider{left:111px;top:3337px;width:972px;height:1px;background:#333}
.copyright{left:0;width:1200px;top:3364px;text-align:center;color:#ddd;font-size:14px}
</style>
</head>
<body>

<!-- HERO -->
<svg class="hero-bg" viewBox="0 0 1200 780" aria-hidden="true">
  <rect x="600" y="0" width="600" height="640" fill="#000"/>
  <path d="M0 0H600V690C560 700 520 680 470 660C430 650 380 700 330 720C300 700 250 660 200 665C150 668 110 640 80 620C60 640 40 655 0 650Z" fill="#d90000"/>
  <path d="M600 640H1200V620C1170 650 1140 680 1100 690C1070 700 1040 680 1010 690C960 700 920 675 880 685C830 690 800 660 760 670C700 680 650 660 600 650Z" fill="#000"/>
  <g fill="#d90000"><circle cx="395" cy="735" r="6"/><circle cx="418" cy="752" r="4"/><circle cx="372" cy="770" r="3"/><circle cx="320" cy="742" r="3"/><circle cx="25" cy="660" r="4"/></g>
  <g fill="#000"><circle cx="820" cy="710" r="5"/><circle cx="860" cy="728" r="3"/><circle cx="930" cy="705" r="4"/><circle cx="1060" cy="720" r="5"/><circle cx="1120" cy="700" r="3"/><circle cx="712" cy="664" r="6"/><circle cx="1185" cy="660" r="4"/></g>
</svg>

<div class="abs brand"><span class="brand-dot"></span>BrimBowl</div>

<div class="abs topbar">
  <span><svg class="icon" viewBox="0 0 24 24"><path d="M2 5h20v14H2z M2 5l10 8 10-8" fill="none" stroke="#fff" stroke-width="2"/></svg> hi@brimbowl.com.au</span>
  <span>|</span>
  <span><svg class="icon" viewBox="0 0 24 24"><path d="M6 2l4 5-2 3c1 3 3 5 6 6l3-2 5 4-2 4C10 22 2 14 2 4z"/></svg> 1800 555 010</span>
</div>

<nav class="abs nav">
  <a class="active" href="#">HOME</a><a href="#">ABOUT</a><a href="#">HISTORY</a><a href="#">MENU</a><a href="#">CONTACT</a>
</nav>

<h1 class="abs heading hero-title">Home<br>Dining<br>Delivery</h1>
<a class="btn btn--white" href="#" style="left:107px;top:480px;width:238px;height:69px;font-size:22px">Order Now</a>
<div class="placeholder hero-bowl" role="img" aria-label="White bowl of beef noodle soup topped with spring onions and herbs"></div>

<!-- WELCOME -->
<div class="placeholder veg" role="img" aria-label="Fresh vegetables tumbling: onions, garlic, ginger, capsicum, chillies and tomatoes"></div>
<h2 class="abs heading welcome-title">Welcome to<br>BrimBowl</h2>
<p class="abs welcome-text">Mai, a third generation barer of her family's Vietnamese ancestry, was born in Saigon, Vietnam (presently known as Ho Chi Minh City). Here, at an early age, she was seeped in the traditions of her family's culture. As a child she would work in the family kitchen side by side with her Ba, Me, and Co's (Grandma, Mother, and Aunts). This is where she was exposed to the discipline of tradition as meals were prepared as they had been by the many generations that had come before her.</p>
<a class="btn btn--red" href="#" style="left:635px;top:1209px;width:186px;height:64px;font-size:19px">Read More</a>
<div class="placeholder avatar" role="img" aria-label="Portrait of the founder"></div>
<div class="placeholder signature" role="img" aria-label="Handwritten signature of Mai Linh"></div>

<!-- MENU -->
<svg class="menu-band" viewBox="0 0 1200 830" aria-hidden="true">
  <defs><linearGradient id="band" x1="0" x2="1"><stop offset="0" stop-color="#efefef"/><stop offset=".5" stop-color="#d8d8d8"/><stop offset="1" stop-color="#cfcfcf"/></linearGradient></defs>
  <path d="M40 90C120 60 200 75 300 55C420 40 520 70 640 48C760 30 900 50 1050 40L1200 40V760C1100 770 1000 745 900 760C760 780 620 750 480 770C340 790 200 760 60 775L40 760C20 600 30 300 40 90Z" fill="url(#band)"/>
  <g fill="#cfcfcf"><circle cx="130" cy="40" r="6"/><circle cx="180" cy="22" r="4"/><circle cx="420" cy="28" r="5"/><circle cx="820" cy="800" r="6"/><circle cx="900" cy="815" r="4"/><circle cx="1120" cy="812" r="5"/><circle cx="760" cy="790" r="3"/></g>
</svg>
<h2 class="abs heading menu-title">Menu</h2>
<h3 class="abs dish-name">Egg Rolls (life changing)</h3>
<div class="abs dish-price">10 FOR $10</div>
<p class="abs dish-text">Our egg rolls are an experience not to be missed. They are provided either prepared and ready to eat or fresh and ready for pan frying at your convenience.<br>We create a wonderfully balanced mix of prawn, chicken, and pork. We start by taking the time to properly Julian slice the carrots (slightly sweet), dry wood ear mushrooms (to enhance the texture), taro (an all-natural and healthy binder for the mix), onion, garlic, and glass noodles are all combined in a beautifully balanced mixture that is hand wrapped in Vietnamese rice paper.</p>
<a class="btn btn--red" href="#" style="left:111px;top:1978px;width:218px;height:62px;font-size:19px">Order Now</a>
<div class="abs menu-contact">
  <svg viewBox="0 0 24 24"><path d="M2 5h20v14H2z"/><path d="M2 5l10 8 10-8" fill="none" stroke="#fff" stroke-width="2"/></svg>
  <span>hi@brimbowl.com.au</span><span>|</span>
  <svg viewBox="0 0 24 24"><path d="M6 2l4 5-2 3c1 3 3 5 6 6l3-2 5 4-2 4C10 22 2 14 2 4z"/></svg>
  <span>1800 555 010</span>
</div>
<a class="abs browse" href="#">BROWSE MENU</a>
<div class="arrow" style="left:570px"><svg viewBox="0 0 16 16"><path d="M10 3L5 8l5 5"/></svg></div>
<div class="arrow" style="left:614px"><svg viewBox="0 0 16 16"><path d="M6 3l5 5-5 5"/></svg></div>
<div class="placeholder rolls" role="img" aria-label="Hands wrapping fresh egg rolls in rice paper on a woven tray lined with banana leaves"></div>

<!-- KEEP IN TOUCH -->
<h2 class="abs heading touch-title">Keep in Touch</h2>
<div class="placeholder leaf" role="img" aria-label="Green banana leaf"></div>
<div class="abs form-card"></div>
<div class="placeholder form-photo" role="img" aria-label="Spoonful of crab and corn soup"></div>

<span class="label" style="left:510px;top:2369px">Name</span>
<div class="field" style="left:512px;top:2397px;width:546px;height:40px"></div>
<span class="label" style="left:510px;top:2449px">Email</span>
<div class="field" style="left:512px;top:2477px;width:259px;height:40px"></div>
<span class="label" style="left:789px;top:2449px">Phone</span>
<div class="field" style="left:790px;top:2477px;width:268px;height:40px"></div>
<span class="label" style="left:510px;top:2528px">Address</span>
<div class="field" style="left:512px;top:2556px;width:546px;height:40px"></div>
<span class="label" style="left:510px;top:2606px">Messsage</span>
<div class="field" style="left:512px;top:2633px;width:546px;height:83px"></div>
<div class="abs agree"><span class="box"></span>I agree to the Terms of Service and Privacy Notices</div>
<a class="btn btn--red" href="#" style="left:505px;top:2778px;width:149px;height:55px;font-size:18px">Submit</a>

<!-- FOOTER -->
<svg class="footer-bg" viewBox="0 0 1200 557" aria-hidden="true">
  <path d="M0 130C60 110 90 125 140 120C260 110 330 140 420 125C520 110 640 135 760 120C860 105 960 90 1050 80C1120 70 1170 60 1200 55V557H0Z" fill="#000"/>
  <g fill="#000"><circle cx="300" cy="30" r="6"/><circle cx="340" cy="60" r="9"/><circle cx="280" cy="75" r="4"/><circle cx="420" cy="40" r="5"/><circle cx="500" cy="80" r="3"/><circle cx="820" cy="50" r="7"/><circle cx="880" cy="30" r="4"/><circle cx="1000" cy="45" r="6"/><circle cx="1080" cy="20" r="4"/><circle cx="230" cy="100" r="5"/><circle cx="760" cy="80" r="5"/></g>
</svg>
<div class="abs foot-heading" style="left:111px;top:3050px">Delivery Areas</div>
<div class="placeholder map" role="img" aria-label="Map of Australia with red pins marking delivery areas"></div>
<div class="abs foot-heading" style="left:513px;top:3050px">Contact Us</div>
<div class="abs foot-line" style="left:513px;top:3099px"><svg class="icon" viewBox="0 0 24 24"><path d="M2 5h20v14H2z"/><path d="M2 5l10 8 10-8" fill="none" stroke="#000" stroke-width="2"/></svg>hi@brimbowl.com.au</div>
<div class="abs foot-line" style="left:513px;top:3157px"><svg class="icon" viewBox="0 0 24 24"><path d="M6 2l4 5-2 3c1 3 3 5 6 6l3-2 5 4-2 4C10 22 2 14 2 4z"/></svg>1800 555 010</div>
<span class="social" style="left:508px" aria-label="Social link"></span>
<span class="social" style="left:554px" aria-label="Social link"></span>
<span class="social" style="left:609px" aria-label="Social link"></span>
<span class="social" style="left:658px" aria-label="Social link"></span>
<span class="social" style="left:711px" aria-label="Snapgrid"></span>
<div class="placeholder noodles" role="img" aria-label="Glass bowl of bean sprouts, lime wedge, chilli and mint"></div>
<div class="abs divider"></div>
<div class="abs copyright">© 2020 BrimBowl. All Rights Reserved.</div>

</body>
</html>
```